Post storm repair flyer

looking for an eye catching 6x9 postcard to send out to single family home owners advertising a "Post Storm Repair Special" explaining that after the recent hurricanes its very important to have your roof checked and any repairs fixed right away before they become a bigger more costly problem and that even though your home wasn't directly hit by the storm the high wind gust could've cause unseen damage.
offer $200 off any repair *some rules may apply
Lark Roofing
888.417.LARK
www.LarkRoofing.example

Roofing

```html
<!DOCTYPE html>
<html lang="en">
<head>
<meta charset="UTF-8">
<title>Lark Roofing – Post-Storm Repair Special Postcard</title>
<link href="https://fonts.googleapis.com/css2?family=Montserrat:ital,wght@0,400;0,500;0,600;0,700;0,800;1,500;1,700;1,800&display=swap" rel="stylesheet">
<style>
  :root{
    --navy:#1c2d4f;
    --navy-deep:#15233f;
    --yellow:#eab530;
    --green:#3cb44a;
    --white:#ffffff;
    --stage:#c9c9c9;
    --line:#1c2d4f;
  }
  *{margin:0;padding:0;box-sizing:border-box;}
  html,body{width:1200px;height:1200px;overflow:hidden;background:var(--stage);}
  body{font-family:"Montserrat",Arial,sans-serif;position:relative;}
  .card{position:absolute;left:191px;width:818px;height:545px;overflow:hidden;background:var(--navy);}
  .card-front{top:50px;}
  .card-back{top:610px;}
  .shapes{position:absolute;inset:0;width:818px;height:545px;}
  .abs{position:absolute;}

  /* front */
  .headline{left:28px;top:31px;color:var(--yellow);font-weight:800;font-size:36px;line-height:33px;letter-spacing:.3px;}
  .tagline{left:29px;top:104px;width:325px;height:24px;background:var(--yellow);color:var(--navy);font-style:italic;font-weight:700;font-size:14px;line-height:24px;padding-left:9px;letter-spacing:.2px;}
  .alert{left:30px;top:148px;color:var(--white);font-weight:800;font-size:19.5px;line-height:23px;letter-spacing:.4px;}
  .alert .hl{color:var(--yellow);}
  .intro{left:30px;top:219px;width:290px;color:var(--white);font-weight:500;font-size:12.6px;line-height:20.3px;}
  .cta{left:30px;top:330px;color:var(--navy);font-weight:800;font-size:21.5px;line-height:21px;letter-spacing:.3px;}
  .receive{left:30px;top:371px;color:var(--navy);font-style:italic;font-weight:700;font-size:14.5px;}
  .receive-rule{left:106px;top:381px;width:290px;height:2px;background:var(--navy);}
  .offer{left:30px;top:390px;width:229px;height:47px;background:var(--navy);color:var(--white);font-weight:800;font-size:37px;line-height:47px;padding-left:10px;letter-spacing:-.5px;}
  .offer .off{color:var(--yellow);}
  .offer-scope{left:266px;top:389px;color:var(--navy);font-weight:800;font-size:19px;line-height:19px;}
  .offer-rules{left:266px;top:426px;color:var(--navy);font-style:italic;font-weight:700;font-size:11px;}
  .call-label{left:30px;top:468px;color:var(--white);font-style:italic;font-weight:700;font-size:15px;}
  .phone{left:30px;top:494px;color:var(--white);font-weight:800;font-size:26px;display:flex;align-items:center;gap:8px;}
  .web{left:258px;top:498px;color:var(--white);font-style:italic;font-weight:700;font-size:15.5px;display:flex;align-items:center;gap:8px;height:24px;}
  .brand-name{left:604px;top:90px;width:170px;text-align:center;color:var(--navy);font-weight:800;font-size:26px;line-height:30px;}

  /* back */
  .why-title{left:33px;top:31px;color:var(--yellow);font-weight:800;font-size:20px;letter-spacing:.3px;}
  .why-title .w{color:var(--white);}
  .reasons{left:33px;top:60px;width:420px;list-style:none;}
  .reasons li{position:relative;padding-left:20px;color:var(--white);font-weight:500;font-size:12.3px;line-height:12.8px;margin-bottom:7.3px;letter-spacing:.3px;}
  .reasons li::before{content:"";position:absolute;left:1px;top:4px;width:13px;height:13px;border-radius:50%;background:var(--yellow);}
  .reasons b{color:var(--yellow);font-weight:700;}
  .services-title{left:31px;top:157px;color:var(--white);font-weight:700;font-size:15.5px;}
  .services-copy{left:32px;top:178px;width:420px;color:var(--white);font-weight:600;font-size:9.6px;line-height:12.6px;letter-spacing:.4px;}
  .services{left:33px;top:233px;list-style:none;}
  .services li{color:var(--white);font-weight:700;font-size:13px;line-height:16.4px;display:flex;align-items:center;gap:7px;letter-spacing:.2px;}
  .footer-mark{left:23px;top:476px;width:40px;height:40px;border-radius:50%;border:3px solid var(--yellow);}
  .footer-info{left:87px;top:466px;color:var(--white);font-style:italic;font-weight:500;font-size:15px;line-height:18px;}
  .pair-label{font-family:"Montserrat",Arial,sans-serif;font-weight:800;font-style:italic;font-size:22px;fill:var(--navy);stroke:var(--white);stroke-width:1.2px;paint-order:stroke;}
</style>
</head>
<body>

<!-- FRONT -->
<section class="card card-front">
  <svg class="shapes" viewBox="0 0 818 545" xmlns="http://www.w3.org/2000/svg">
    <defs>
      <linearGradient id="gNavy" x1="0" y1="0" x2="1" y2="1">
        <stop offset="0" stop-color="#223659"/><stop offset="1" stop-color="#17264a"/>
      </linearGradient>
      <linearGradient id="gRoofPhoto" x1="0" y1="0" x2="0" y2="1">
        <stop offset="0" stop-color="#b9cde0"/><stop offset=".4" stop-color="#8fa3b6"/><stop offset=".7" stop-color="#5d5a5a"/><stop offset="1" stop-color="#3d3a3c"/>
      </linearGradient>
      <linearGradient id="gStrip" x1="0" y1="0" x2="0" y2="1">
        <stop offset="0" stop-color="#7fa2c4"/><stop offset=".55" stop-color="#5d5a52"/><stop offset="1" stop-color="#3a3c42"/>
      </linearGradient>
    </defs>
    <rect width="818" height="545" fill="url(#gNavy)"/>
    <polygon points="428,0 552,0 458,316 292,316" fill="var(--green)"/>
    <polygon points="432,0 548,0 517,102 388,102" fill="url(#gStrip)" role="img" aria-label="Photo: roofer kneeling on shingles"/>
    <polygon points="386,106 516,106 486,208 342,208" fill="url(#gStrip)" role="img" aria-label="Photo: roofer fitting shingles"/>
    <polygon points="340,212 484,212 454,314 296,314" fill="url(#gStrip)" role="img" aria-label="Photo: roofer in cap repairing a roof"/>
    <polygon points="0,316 470,316 412,385 460,453 0,453" fill="var(--yellow)"/>
    <rect x="0" y="330" width="13" height="111" fill="var(--green)"/>
    <polygon points="540,0 580,0 480,385 564,545 530,545 412,385 470,316" fill="var(--green)"/>
    <polygon points="568,0 818,0 818,545 560,545 470,385" fill="url(#gRoofPhoto)" role="img" aria-label="Photo: two roofers in hard hats repairing a shingle roof"/>
  </svg>

  <h1 class="abs headline">POST-STORM<br>REPAIR SPECIAL!</h1>
  <p class="abs tagline">Protect Your Home Before It's Too Late</p>
  <h2 class="abs alert">HURRICANE WINDS<br><span class="hl">COULD HAVE DAMAGED</span><br>YOUR <span class="hl">ROOF!</span></h2>
  <p class="abs intro">Even if your home wasn't directly hit, high wind gusts from recent storms could have caused unseen damage. Don’t wait until small issues turn into costly problems!</p>
  <h2 class="abs cta">GET YOUR ROOF CHECKED<br>AND REPAIRED NOW!</h2>
  <p class="abs receive">Receive</p>
  <div class="abs receive-rule"></div>
  <p class="abs offer">$200 <span class="off">OFF</span></p>
  <p class="abs offer-scope">ANY ROOF<br>REPAIR</p>
  <p class="abs offer-rules">*some rules may apply</p>
  <p class="abs call-label">Call Us Today:</p>
  <p class="abs phone">
    <svg width="20" height="22" viewBox="0 0 24 24" fill="none" stroke="#fff" stroke-width="2.2" stroke-linecap="round"><path d="M6 3l3 4-2 2c1 3 4 6 7 7l2-2 4 3-2 3C10 20 4 14 3 5z"/><path d="M14 4a6 6 0 0 1 6 6M14 8a2 2 0 0 1 2 2"/></svg>
    000 1234 567
  </p>
  <p class="abs web">
    <svg width="20" height="20" viewBox="0 0 24 24" fill="none" stroke="#fff" stroke-width="1.6"><circle cx="12" cy="12" r="10"/><ellipse cx="12" cy="12" rx="4.5" ry="10"/><path d="M2 12h20M4 6.5h16M4 17.5h16"/></svg>
    www.LarkRoofing.example
  </p>
  <p class="abs brand-name">Lark Roofing</p>
</section>

<!-- BACK -->
<section class="card card-back">
  <svg class="shapes" viewBox="0 0 818 545" xmlns="http://www.w3.org/2000/svg">
    <defs>
      <linearGradient id="gNavyBack" x1="0" y1="0" x2="1" y2="1">
        <stop offset="0" stop-color="#223659"/><stop offset="1" stop-color="#16254a"/>
      </linearGradient>
      <linearGradient id="gBefore" x1="0" y1="0" x2="1" y2="1">
        <stop offset="0" stop-color="#8d96a3"/><stop offset=".5" stop-color="#b8bec6"/><stop offset="1" stop-color="#6c7380"/>
      </linearGradient>
      <linearGradient id="gAfter" x1="0" y1="0" x2="0" y2="1">
        <stop offset="0" stop-color="#7a8290"/><stop offset="1" stop-color="#4f5663"/>
      </linearGradient>
    </defs>
    <rect width="818" height="545" fill="url(#gNavyBack)"/>
    <polygon points="0,316 475,316 445,443 0,443" fill="var(--yellow)"/>
    <polygon points="6,326 228,326 218,439 0,439" fill="var(--white)"/>
    <polygon points="13,331 220,331 211,433 9,433" fill="url(#gBefore)" role="img" aria-label="Photo: storm-damaged shingles with missing pieces"/>
    <polygon points="231,326 442,326 432,439 216,439" fill="var(--white)"/>
    <polygon points="238,331 435,331 426,433 225,433" fill="url(#gAfter)" role="img" aria-label="Photo: newly repaired shingle roof"/>
    <text class="pair-label" x="56" y="420">BEFORE</text>
    <text class="pair-label" x="284" y="420">AFTER</text>
    <polygon points="508,0 550,0 426,545 415,545" fill="var(--green)"/>
    <polygon points="548,0 818,0 818,545 424,545" fill="var(--white)"/>
    <rect x="669.5" y="34.5" width="112" height="127" fill="none" stroke="#888" stroke-width="1"/>
    <g stroke="var(--line)" stroke-width="1">
      <line x1="505" y1="249.5" x2="784" y2="249.5"/>
      <line x1="505" y1="292.5" x2="784" y2="292.5"/>
      <line x1="505" y1="335.5" x2="784" y2="335.5"/>
      <line x1="505" y1="378.5" x2="784" y2="378.5"/>
      <line x1="505" y1="422.5" x2="784" y2="422.5"/>
    </g>
  </svg>

  <h2 class="abs why-title">WHY YOU SHOULD <span class="w">ACT NOW:</span></h2>
  <ul class="abs reasons">
    <li><b>Prevent Leaks &amp; Water Damage:</b> Even minor damage can lead to leaks, mold, and expensive repairs.</li>
    <li><b>Protect Your Investment:</b> Your home is one of your biggest investments—keep it safe and secure.</li>
    <li><b>Peace of Mind:</b> A thorough roof inspection gives you confidence that your home is storm-ready.</li>
  </ul>
  <h3 class="abs services-title">Our Services</h3>
  <p class="abs services-copy">Lark Roofing offers an array of roofing solutions while providing professional, honest recommendations that address your specific needs. You can always count on us for exceptional service from the moment we meet. From inspection to installation, LARK has you covered.</p>
  <ul class="abs services">
    <li><svg width="12" height="12" viewBox="0 0 24 24" fill="none" stroke="var(--yellow)" stroke-width="3"><circle cx="12" cy="12" r="10"/><path d="M7 12l3.5 3.5L17 9"/></svg>Retail/Commercial Roof Replacement</li>
    <li><svg width="12" height="12" viewBox="0 0 24 24" fill="none" stroke="var(--yellow)" stroke-width="3"><circle cx="12" cy="12" r="10"/><path d="M7 12l3.5 3.5L17 9"/></svg>Storm Damage Roof Replacement</li>
    <li><svg width="12" height="12" viewBox="0 0 24 24" fill="none" stroke="var(--yellow)" stroke-width="3"><circle cx="12" cy="12" r="10"/><path d="M7 12l3.5 3.5L17 9"/></svg>New Construction</li>
    <li><svg width="12" height="12" viewBox="0 0 24 24" fill="none" stroke="var(--yellow)" stroke-width="3"><circle cx="12" cy="12" r="10"/><path d="M7 12l3.5 3.5L17 9"/></svg>Repairs &amp; Restoration</li>
  </ul>
  <div class="abs footer-mark"></div>
  <p class="abs footer-info">LARK Home Group LLC | P: 888.417.LARK<br>4120 Meridian Pkwy, Ste C4<br>Lakeview, GA 30099</p>
</section>

</body>
</html>
```